Electrical Contractor Company Profile

We need a Brochure that is more entertaining than our current Company Profile Document. We have lots of great experience and awesome looking jobs in our portfolio but need a document that we can either print of send in electronic format to accompany some of our submissions.

We are ideally looking for something 9-10 pages in A4 with some of the pages opening out to A3.

We are looking for a document that is professional and smart however shows the colour and quality that we feel we offer to prospective clientele.

I have included the current Company Profile and Logo along with a number of images of completed projects that may be of use.

Target Market(s)

Builders, Facility Managers, Engineers, Decision makers

Industry/Entity Type

Electrical

Font styles to use
Sans Serif

Colors

Designer to choose colors to be used in the design.

Requirements
Must have
• - Modern look with a focus on sustainability
• - Clean Simple and Professional
• - Incorporate our Logo
• Core Business Lines need to be across an A3 opening page and have photos relating to these lines Solar, Communications and any of the projects.
Nice to have
• Lots of colour and photos mixed with the text
Should not have
• Lightning bolts or corny symbols

```html
<!DOCTYPE html>
<html lang="en">
<head>
<meta charset="utf-8">
<title>Voltara Electrical – Contact</title>
<link rel="stylesheet" href="https://fonts.googleapis.com/css2?family=Barlow:wght@400;500;600;700&display=swap">
<style>
  :root {
    --navy: #0a1f47;
    --navy-soft: #14305e;
    --icon-blue: #0f3b70;
    --orange: #f07722;
    --white: #ffffff;
  }
  html, body {
    margin: 0;
    padding: 0;
    width: 849px;
    height: 1200px;
    overflow: hidden;
    background: var(--white);
  }
  .back-cover {
    position: relative;
    width: 849px;
    height: 1200px;
    overflow: hidden;
    font-family: "Barlow", sans-serif;
    color: var(--navy);
  }
  .back-cover__band {
    position: absolute;
    inset: 0;
  }
  .back-cover__texture {
    position: absolute;
    left: 0;
    top: 0;
    width: 125px;
    height: 360px;
    background: linear-gradient(160deg, rgba(40, 78, 130, 0.55), rgba(20, 48, 94, 0));
  }
  .contact {
    position: absolute;
    left: 121px;
    top: 726px;
  }
  .contact__title {
    margin: 0;
    font-size: 23px;
    font-weight: 700;
    letter-spacing: 0.3px;
    line-height: 1;
  }
  .contact__rule {
    width: 57px;
    height: 4px;
    background: var(--orange);
    margin-top: 24px;
  }
  .contact__item {
    position: absolute;
    font-size: 13.5px;
    line-height: 19px;
    white-space: nowrap;
  }
  .contact__item--address { left: 0; top: 108px; font-weight: 500; }
  .contact__item--phones { left: 0; top: 186px; font-weight: 700; }
  .contact__item--email { left: 0; top: 224px; font-weight: 700; }
  .contact__icon {
    position: absolute;
    width: 27px;
    height: 27px;
  }
  .contact__icon--pin { left: 73px; top: 833px; }
  .contact__icon--phone { left: 77px; top: 911px; }
  .contact__icon--email { left: 80px; top: 947px; }
  .contact__web {
    position: absolute;
    left: 121px;
    top: 1005px;
    margin: 0;
    font-size: 19px;
    font-weight: 600;
    font-style: italic;
    color: var(--orange);
  }
  .brand {
    position: absolute;
    left: 477px;
    top: 988px;
    display: flex;
    align-items: center;
    gap: 16px;
  }
  .brand__mark {
    width: 62px;
    height: 62px;
    border-radius: 50%;
    border: 4px solid var(--orange);
    box-sizing: border-box;
  }
  .brand__name {
    font-size: 34px;
    font-weight: 700;
    color: var(--orange);
    letter-spacing: 0.5px;
    line-height: 1;
  }
</style>
</head>
<body>
<main class="back-cover">
  <svg class="back-cover__band" width="849" height="1200" viewBox="0 0 849 1200" aria-hidden="true">
    <polygon fill="var(--navy)" points="0,0 337,0 337,157 849,593 849,1200 445,1200 445,768 0,390"/>
  </svg>
  <div class="back-cover__texture" role="img" aria-label="Decorative dot pattern in soft blue tones"></div>

  <section class="contact">
    <h2 class="contact__title">CONTACT US</h2>
    <div class="contact__rule"></div>
    <p class="contact__item contact__item--address" style="margin:0">24 Carrow Lane<br>Westhaven WA 6010</p>
    <p class="contact__item contact__item--phones" style="margin:0">1300 555 214<br>08 5550 1487</p>
    <p class="contact__item contact__item--email" style="margin:0">hello@voltarawa.com.au</p>
  </section>

  <svg class="contact__icon contact__icon--pin" viewBox="0 0 27 27" aria-hidden="true">
    <circle cx="13.5" cy="13.5" r="13.5" fill="var(--icon-blue)"/>
    <path d="M13.5 6.5a4.8 4.8 0 0 0-4.8 4.8c0 3.6 4.8 9 4.8 9s4.8-5.4 4.8-9a4.8 4.8 0 0 0-4.8-4.8z" fill="var(--orange)"/>
    <circle cx="13.5" cy="11.3" r="1.8" fill="var(--icon-blue)"/>
  </svg>
  <svg class="contact__icon contact__icon--phone" viewBox="0 0 27 27" aria-hidden="true">
    <circle cx="13.5" cy="13.5" r="13.5" fill="var(--icon-blue)"/>
    <path d="M11 7.5l2 3.2-1.4 1.3c.6 1.6 1.7 2.8 3.2 3.6l1.3-1.4 3.2 2-1.1 2.3c-4.6-.5-8.3-4.6-8.6-9.2z" fill="var(--orange)"/>
  </svg>
  <svg class="contact__icon contact__icon--email" viewBox="0 0 27 27" aria-hidden="true">
    <circle cx="13.5" cy="13.5" r="13.5" fill="var(--icon-blue)"/>
    <text x="13.5" y="18.5" text-anchor="middle" font-family="Barlow, sans-serif" font-size="15" font-weight="500" fill="var(--orange)">@</text>
  </svg>

  <p class="contact__web">www.voltarawa.com.au</p>

  <div class="brand">
    <span class="brand__mark" aria-hidden="true"></span>
    <span class="brand__name">VOLTARA ELECTRICAL</span>
  </div>
</main>
</body>
</html>
```